I need a book cover for a 6x9 book. The front cover information (title and author) is below, and the back cover information will be given to the winning designer. I am wanting something vibrant and bright, and I am open to your creativity, but I do not want any pictures of people on the cover. Save room for the barcode on the back cover.
Title:
Oops! Wrong Turn?
Quiet Rooms Explained: Notes on Patient Gardening Habits
Author:
Marisol Tembe

```html
<!DOCTYPE html>
<html lang="en">
<head>
<meta charset="utf-8">
<title>Oops! Wrong Turn? — Book Cover</title>
<link rel="stylesheet" href="https://fonts.googleapis.com/css2?family=Bebas+Neue&family=Montserrat:wght@500&display=swap">
<style>
  :root {
    --page: #ffffff;
    --cover-red: #c0000e;
    --cover-red-deep: #ad000c;
    --panel-light: #f8f6f3;
    --panel-warm: #eee1b8;
    --ink: #000000;
    --accent-yellow: #f5d400;
    --text-light: #ffffff;
  }
  html, body {
    margin: 0;
    padding: 0;
    width: 1200px;
    height: 1200px;
    overflow: hidden;
    background: var(--page);
  }
  .cover-canvas {
    display: block;
    width: 1200px;
    height: 1200px;
  }
  .title {
    font-family: "Bebas Neue", "Oswald", sans-serif;
    fill: var(--ink);
  }
  .subtitle, .author {
    font-family: "Montserrat", "Helvetica Neue", sans-serif;
    font-weight: 500;
  }
  .subtitle-lead { fill: var(--text-light); }
  .subtitle-tail { fill: var(--accent-yellow); }
  .author { fill: var(--text-light); }
</style>
</head>
<body>
<svg class="cover-canvas" viewBox="0 0 1416 1416" xmlns="http://www.w3.org/2000/svg">
  <defs>
    <radialGradient id="cover-glow" cx="50%" cy="45%" r="70%">
      <stop offset="0%" stop-color="var(--cover-red)"/>
      <stop offset="100%" stop-color="var(--cover-red-deep)"/>
    </radialGradient>
    <radialGradient id="artwork-tone" cx="55%" cy="45%" r="65%">
      <stop offset="0%" stop-color="var(--panel-light)"/>
      <stop offset="70%" stop-color="var(--panel-light)"/>
      <stop offset="100%" stop-color="var(--panel-warm)"/>
    </radialGradient>
  </defs>

  <g class="book-cover">
    <rect class="cover-base" x="261" y="38" width="900" height="1350" fill="url(#cover-glow)"/>

    <rect class="cover-artwork" x="306" y="112" width="818" height="846" rx="60"
          fill="url(#artwork-tone)" role="img"
          aria-label="Illustration: large cream speech bubble surrounded by question marks and small sparkles"/>

    <text class="title title-top" x="420" y="566" font-size="318" textLength="598" lengthAdjust="spacingAndGlyphs">OOPS!</text>
    <text class="title title-bottom" x="424" y="710" font-size="172" textLength="596" lengthAdjust="spacingAndGlyphs">WRONG TURN?</text>

    <text class="subtitle subtitle-lead" x="711" y="1093" font-size="40" text-anchor="middle">Quiet Rooms Explained:</text>
    <text class="subtitle subtitle-tail" x="711" y="1152" font-size="40" text-anchor="middle">Notes on Patient Gardening Habits</text>

    <text class="author" x="733" y="1310" font-size="70" text-anchor="middle">Marisol Tembe</text>
  </g>
</svg>
</body>
</html>
```